New Business Cards for MB&LR

We need updated business cards for a staff of 15 engineers, estimators, project managers, and sales people. We have recently begun changes to our website and marketing material to improve our look and branding. We are an established fabricator specializing in pressure vessels, tanks, and structural steel. The owners require us to use the existing logo and old english text design. Also, we prefer dark grey or mostly black cards.
Target Market(s)
Engineers, purchasing agents, estimators, and project managers of; mining companies, refineries, industrial construction professionals
Industry/Entity Type
Business
Contact Information for Business Card
Logo, phone, website, email, etc.
Look and feel

```html
<!DOCTYPE html>
<html lang="en">
<head>
<meta charset="utf-8">
<title>MB&amp;LR Business Cards</title>
<link rel="stylesheet" href="https://fonts.googleapis.com/css2?family=Open+Sans:wght@400;600;700&family=Tinos:ital,wght@0,400;0,700;1,400&display=swap">
<style>
  :root {
    --stage: #e9e6e3;
    --card-white: #ffffff;
    --ink: #111111;
    --band: #000000;
    --paper-on-dark: #ffffff;
    --rule: #333333;
    --shadow: rgba(0,0,0,0.25);
  }
  * { margin: 0; padding: 0; box-sizing: border-box; }
  html, body { width: 1200px; height: 900px; overflow: hidden; }
  body { background: var(--stage); position: relative; font-family: "Open Sans", Arial, sans-serif; color: var(--ink); }

  .card { position: absolute; width: 588px; height: 362px; box-shadow: 0 6px 18px var(--shadow); }
  .card--front { left: 258px; top: 78px; background: var(--card-white); }
  .card--back { left: 518px; top: 492px; background: var(--band); }

  .band { position: absolute; left: 0; top: 42px; width: 100%; height: 112px; }

  .company-name {
    position: absolute; left: 0; width: 100%; top: 168px; text-align: center;
    font-family: "Tinos", serif; font-weight: 400; font-size: 22px; line-height: 1;
  }
  .company-name span { display: inline-block; padding: 0 2px 3px; border-bottom: 1.5px solid var(--ink); }
  .tagline {
    position: absolute; left: 0; width: 100%; top: 199px; text-align: center;
    font-family: "Tinos", serif; font-style: italic; font-size: 16px;
  }

  .person { position: absolute; right: 297px; top: 241px; text-align: right; }
  .person__name { font-family: "Tinos", serif; font-weight: 700; font-size: 19px; line-height: 24px; }
  .person__role { font-size: 14px; line-height: 20px; }
  .person__email { font-size: 14px; line-height: 22px; display: flex; align-items: center; justify-content: flex-end; gap: 6px; }

  .divider { position: absolute; left: 298px; top: 242px; width: 1.5px; height: 58px; background: var(--rule); }

  .contacts { position: absolute; left: 314px; top: 241px; list-style: none; }
  .contacts li { font-size: 14px; line-height: 21px; display: flex; align-items: center; gap: 7px; }
  .icon { width: 11px; height: 11px; flex: none; }

  .address { position: absolute; left: 0; width: 100%; top: 318px; text-align: center; font-size: 14px; }

  .brand-name {
    position: absolute; font-family: "Open Sans", Arial, sans-serif; font-weight: 700;
    color: var(--paper-on-dark); text-align: center; line-height: 1;
  }
  .brand-name--front { left: 200px; width: 188px; top: 84px; font-size: 26px; }
  .brand-name--back { left: 0; width: 100%; top: 158px; font-size: 46px; }
</style>
</head>
<body>
  <section class="card card--front" aria-label="Business card front">
    <svg class="band" viewBox="0 0 588 112" aria-hidden="true">
      <rect x="0" y="0" width="588" height="112" fill="var(--band)"/>
      <rect x="36" y="28" width="148" height="56" rx="4" fill="none" stroke="var(--card-white)" stroke-width="2"/>
      <rect x="410" y="20" width="80" height="72" rx="10" fill="none" stroke="var(--card-white)" stroke-width="2"/>
      <rect x="498" y="24" width="28" height="28" rx="4" fill="none" stroke="var(--card-white)" stroke-width="2"/>
      <rect x="532" y="24" width="28" height="28" rx="4" fill="none" stroke="var(--card-white)" stroke-width="2"/>
      <rect x="498" y="58" width="28" height="28" rx="4" fill="none" stroke="var(--card-white)" stroke-width="2"/>
      <rect x="532" y="58" width="28" height="28" rx="4" fill="none" stroke="var(--card-white)" stroke-width="2"/>
    </svg>
    <div class="brand-name brand-name--front">MB&amp;LR</div>

    <h1 class="company-name"><span>Mesa Boiler &amp; Load Rigging</span></h1>
    <p class="tagline">The Industrial Fabricator</p>

    <div class="person">
      <p class="person__name">Daniel Harper</p>
      <p class="person__role">Managing Director</p>
      <p class="person__email">hello@mbandlr.com
        <svg class="icon" viewBox="0 0 12 12" aria-hidden="true"><rect x="1" y="3" width="10" height="7" fill="var(--ink)"/><path d="M1 3 L6 7 L11 3" stroke="#fff" fill="none" stroke-width="1"/></svg>
      </p>
    </div>
    <div class="divider"></div>
    <ul class="contacts">
      <li>
        <svg class="icon" viewBox="0 0 12 12" aria-hidden="true"><path d="M1 5 Q6 0 11 5 L9 6 L8 4 Q6 3 4 4 L3 6 Z" fill="var(--ink)"/><rect x="3" y="6" width="6" height="5" rx="1" fill="var(--ink)"/></svg>
        555.310.4827
      </li>
      <li>
        <svg class="icon" viewBox="0 0 12 12" aria-hidden="true"><rect x="1" y="4" width="10" height="7" rx="1" fill="var(--ink)"/><rect x="3" y="1" width="6" height="4" fill="var(--ink)"/><rect x="3" y="6" width="6" height="1" fill="#fff"/><rect x="3" y="8" width="6" height="1" fill="#fff"/></svg>
        555.310.4890
      </li>
      <li>
        <svg class="icon" viewBox="0 0 12 12" aria-hidden="true"><circle cx="6" cy="6" r="5.5" fill="var(--ink)"/><path d="M6 1 Q3 6 6 11 M6 1 Q9 6 6 11 M1 6 H11" stroke="#fff" fill="none" stroke-width="0.8"/></svg>
        www.mbandlr.com
      </li>
    </ul>

    <p class="address">740 Ridge Road, PO Box 318220, Cedar Flats City, 84920</p>
  </section>

  <section class="card card--back" aria-label="Business card back">
    <div class="brand-name brand-name--back">MB&amp;LR</div>
  </section>
</body>
</html>
```